Newsletter Header - Insert Cutting Branch

We have a Hollis Grant Foundation (HGF) Logo (see attached) and are creating a Newsletter with the title: The Green Ledger. The founders of the HGF were nursery people and started their plants via cuttings. So, we want to take a branch from the HGF logo tree and attach it somewhere in the Newsletter title. You can leave the logo as it is - just want a cutting somewhere in the title. The Green Ledger title should be 3-D
Updates

Target Market(s)

Donors to our Foundation

Industry/Entity Type

Non Profit

Colors

Designer to choose colors to be used in the design.

Requirements
Must have
• Logo remain as is - just a branch duplicate on the header.
Nice to have
• The Green Ledger would be nice to have as a 3-D image

```html
<!DOCTYPE html>
<html lang="en">
<head>
<meta charset="utf-8">
<title>The Green Ledger – Hollis Grant Foundation Newsletter</title>
<link href="https://fonts.googleapis.com/css2?family=Montserrat:wght@300;400;500;600;700&family=Rye&display=swap" rel="stylesheet">
<style>
:root{
  --page:#eeeced;
  --card:#ffffff;
  --green:#1a9e45;
  --green-dark:#14833a;
  --green-photo:#3f9a4e;
  --text:#555555;
  --muted:#444444;
  --rule:#d9d9d9;
  --alert:#c41e3a;
  --icon:#9a9a9a;
}
*{margin:0;padding:0;box-sizing:border-box}
html,body{width:1200px;height:2291px;overflow:hidden}
body{background:var(--page);font-family:"Montserrat",sans-serif;color:var(--text);position:relative}
.abs{position:absolute}
.preheader{left:0;width:1200px;top:133px;text-align:center;font-family:Arial,Helvetica,sans-serif;font-size:20px;line-height:26px;color:var(--muted)}
.preheader a{color:var(--alert);text-decoration:underline}
.card{left:232px;top:219px;width:739px;height:1697px;background:var(--card);border-radius:18px;overflow:hidden}
.masthead{left:0;top:0;width:739px;height:223px;display:flex}
.masthead-brand{width:180px;height:223px;background:var(--green);display:flex;align-items:center;justify-content:center}
.brand-mark{width:104px;height:104px;border:4px solid #fff;border-radius:50%;display:flex;align-items:center;justify-content:center;text-align:center;color:#fff;font-weight:700;font-size:13px;line-height:16px}
.masthead-banner{flex:1;position:relative;background:radial-gradient(circle at 30% 40%,#5fb865,#2f8a3f 70%);display:flex;align-items:center;justify-content:center}
.masthead-title{font-family:"Rye",serif;font-size:50px;color:#fff;letter-spacing:1px;text-shadow:0 4px 0 #1d6b2b}
/* sections use card coordinates */
.photo-hero{left:27px;top:273px;width:260px;height:213px;background:linear-gradient(160deg,#3f9ea0,#8fbfa6)}
.photo-badge{left:67px;top:467px;width:127px;height:45px;background:#fff;display:flex;align-items:center;gap:5px;padding-left:4px}
.badge-dot{width:36px;height:36px;border:2px solid #333;border-radius:50%;flex:none}
.badge-name{font-size:9px;line-height:11px;color:#333;font-weight:500}
.intro{left:324px;top:270px;width:400px}
.intro h2{font-size:21px;font-weight:700;color:var(--green);line-height:28px;margin-bottom:12px}
.intro p{font-size:17px;line-height:30px;font-weight:400}
.btn{display:flex;align-items:center;justify-content:center;background:var(--green);color:#fff;text-decoration:none;height:52px}
.btn-site{left:324px;top:446px;width:265px;font-size:19px;font-weight:500;gap:12px}
.invite{left:28px;top:543px;width:679px;height:183px;background:var(--green);display:flex;align-items:center}
.invite-icon{margin-left:120px;width:126px;height:146px;background:rgba(255,255,255,.85);border-radius:50% 50% 30% 30%}
.invite h2{margin-left:64px;color:#fff;font-size:29px;line-height:36px;font-weight:700}
.grants{left:27px;top:770px;width:683px}
.grants h2{text-align:center;font-size:21px;line-height:28px;font-weight:700;color:var(--green);padding:0 25px;margin-bottom:12px}
.grants p{font-size:17px;line-height:30px}
.btn-cta{top:978px;width:237px;font-size:18px;font-weight:700;letter-spacing:.5px}
.rule{left:27px;width:678px;height:1px;background:var(--rule)}
.story{left:29px;top:1114px;width:395px}
.story p{font-size:17px;line-height:30px}
.story a{display:block;margin-top:10px;color:var(--green);font-weight:600;font-size:17px;text-decoration:none}
.photo-story{left:448px;top:1115px;width:260px;height:213px;background:linear-gradient(135deg,#6aa34a,#c58860 55%,#b53a3a)}
.footer{left:0;top:1448px;width:739px;text-align:center}
.footer-mark{display:inline-flex;align-items:center;gap:8px}
.footer-mark .badge-dot{width:52px;height:52px}
.footer-mark span{font-size:13px;line-height:15px;color:#333;text-align:left;font-weight:500}
.footer h3{margin-top:10px;color:var(--green);font-size:19px;font-weight:700}
.social{display:flex;justify-content:center;gap:7px;margin-top:12px}
.social span{width:51px;height:51px;border:3px solid var(--icon);border-radius:50%;display:flex;align-items:center;justify-content:center;font-size:11px;color:var(--icon);font-weight:600}
.unsub{margin-top:18px;font-size:18px;color:var(--muted)}
.unsub a{color:var(--green);font-weight:700}
</style>
</head>
<body>
<div class="abs preheader">Is this email not displaying correctly?<br><a href="#">View it in your browser.</a></div>

<main class="abs card">
  <header class="abs masthead">
    <div class="masthead-brand"><div class="brand-mark">Hollis Grant Foundation</div></div>
    <div class="masthead-banner" role="img" aria-label="Rows of potted succulents seen from above">
      <h1 class="masthead-title">THE GREEN LEDGER</h1>
    </div>
  </header>

  <div class="abs photo-hero" role="img" aria-label="Child in a pilot cap wearing cardboard wings against a teal sky"></div>
  <div class="abs photo-badge"><span class="badge-dot"></span><span class="badge-name">Hollis Grant Foundation</span></div>

  <section class="abs intro">
    <h2>We contibute for Changing Lives</h2>
    <p>We are invested in the success of the charitable organizations benefiting from our grants and the charitable causes they support.</p>
  </section>
  <a class="abs btn btn-site" href="#">Watch Our Website
    <svg width="16" height="16" viewBox="0 0 16 16"><circle cx="8" cy="8" r="8" fill="#fff"/><path d="M6.5 4.5 10 8l-3.5 3.5" stroke="#1a9e45" stroke-width="2.2" fill="none"/></svg></a>

  <section class="abs invite">
    <div class="invite-icon" role="img" aria-label="Hands holding a young tree"></div>
    <h2>You're Invited to<br>Our Community</h2>
  </section>

  <section class="abs grants">
    <h2>Hollis Grant Foundation Grantmaking for Charitable Organizations</h2>
    <p>The Hollis Grant Foundation is a private foundation which provides support to organizations that take care of human services and needs throughout the United States. We excel at identifying non-profit corporations which have the expertise to create measurable change in their communities.</p>
  </section>
  <a class="abs btn btn-cta" style="left:87px" href="#">DONATE</a>
  <a class="abs btn btn-cta" style="left:346px" href="#">STAY IN TOUCH</a>

  <div class="abs rule" style="top:1078px"></div>

  <section class="abs story">
    <p>Harold and Mae operated the Harold Hollis Nursery for several decades which became the largest wholesale nursery in the state of Oregon during its time. Their motto was "Quality is our Specialty" and their plant material was heavily ...</p>
    <a href="#">Read More &gt;</a>
  </section>
  <div class="abs photo-story" role="img" aria-label="Mother and daughter blowing soap bubbles in a garden"></div>

  <div class="abs rule" style="top:1407px"></div>

  <footer class="abs footer">
    <div class="footer-mark"><span class="badge-dot"></span><span>Hollis<br>Grant<br>Foundation</span></div>
    <h3>Hollis Grant foundation</h3>
    <div class="social"><span>Feed</span><span>Pics</span></div>
    <p class="unsub">To no longer receive emails from HGL: <a href="#">Unsubscribe.</a></p>
  </footer>
</main>
</body>
</html>
```